Innovation Company Business Card Design

I need to have my business card updated. The current card was designed when the company started 2.5 years ago and was a quick and dirty job.

I need a new card design that is more professional and has my updated company tag line.

I will include the old card's Corel Draw file, and EPS versions as examples of the current design. I will also include the company logo eps and corel version files.

The company pantone colour is pantone 1805 c (a dark red)

I want the design to convey the nature of our business as a strategic technology innovation company, but yet still be professional. We are funky vibey and work from an industrial style office in a vibey designer dominat part of town. Though are clients include large banks and corporate clients too.

The information that needs to be on the card is in attached word document (but doesn't have to be in this order or format)

Final version needs to be supplied in PNG preview, as well as PSD file format (or other editable file version) so that personal information on card can be easily edited and reprinted.

Target Market(s)

CEO's of small to medium size companies
Marketing Managers of large coporates
Account managers of Digital Agencies

Industry/Entity Type

Business

Requirements
Must have
• 86x54mm will be cut in rounded corner credit card size format (Except if you recommend otherwise in your design)
Nice to have
• Some kind of background transparency combined with the pantone colour that gives the card some dimension and depth. But no gradient fills please :-)
Should not have
• Basic gradient fills
• Clipart

```html
<!DOCTYPE html>
<html lang="en">
<head>
<meta charset="utf-8">
<title>Velarix Business Card</title>
<link href="https://fonts.googleapis.com/css2?family=Arimo:wght@400;700&display=swap" rel="stylesheet">
<style>
  :root {
    --brand-red: #a8232b;
    --brand-red-deep: #951d25;
    --paper: #ffffff;
    --ink: #1c1c1c;
    --backdrop: #c9cacc;
    --rule: #222222;
  }
  * { box-sizing: border-box; margin: 0; padding: 0; }
  html, body {
    width: 1200px;
    height: 900px;
    overflow: hidden;
    background: var(--backdrop);
    font-family: "Arimo", Arial, sans-serif;
  }
  .canvas {
    position: relative;
    width: 1200px;
    height: 900px;
  }
  .card {
    position: absolute;
    left: 300px;
    width: 600px;
    height: 377px;
    border-radius: 34px;
    overflow: hidden;
    box-shadow: 0 6px 18px rgba(0, 0, 0, 0.18);
  }

  /* Front */
  .card--front {
    top: 48px;
    background: var(--brand-red);
  }
  .front__brand {
    position: absolute;
    left: 96px;
    top: 118px;
    display: flex;
    flex-direction: column;
    align-items: flex-end;
  }
  .front__name {
    color: var(--paper);
    font-weight: 700;
    font-size: 78px;
    line-height: 1;
    letter-spacing: -1px;
  }
  .front__tagline {
    margin-top: 6px;
    margin-right: 6px;
    color: var(--paper);
    font-weight: 400;
    font-size: 17px;
  }
  .front__url-bar {
    position: absolute;
    left: 96px;
    right: 72px;
    top: 262px;
    height: 26px;
    background: var(--paper);
    display: flex;
    align-items: center;
    justify-content: center;
  }
  .front__url {
    color: var(--brand-red);
    font-size: 14px;
    letter-spacing: 9px;
    font-weight: 400;
  }

  /* Back */
  .card--back {
    top: 475px;
    background: var(--paper);
  }
  .back__mark {
    position: absolute;
    left: 70px;
    top: 120px;
    width: 138px;
    height: 138px;
    background: var(--brand-red);
  }
  .back__divider {
    position: absolute;
    left: 252px;
    top: 92px;
    width: 2px;
    height: 196px;
    background: var(--rule);
  }
  .back__details {
    position: absolute;
    left: 284px;
    top: 96px;
    color: var(--ink);
    font-size: 15px;
    line-height: 1.22;
  }
  .back__person {
    color: var(--brand-red);
    font-weight: 700;
    font-size: 21px;
  }
  .back__role { margin-bottom: 16px; }
  .back__accent { color: var(--brand-red); }
  .back__contact { margin-bottom: 14px; }
  .back__company {
    color: var(--brand-red);
    font-weight: 700;
    font-size: 16px;
  }
</style>
</head>
<body>
<main class="canvas">
  <section class="card card--front" aria-label="Card front">
    <div class="front__brand">
      <h1 class="front__name">Velarix</h1>
      <p class="front__tagline">Strategic Innovation</p>
    </div>
    <div class="front__url-bar">
      <span class="front__url">www.velarix.com</span>
    </div>
  </section>

  <section class="card card--back" aria-label="Card back">
    <div class="back__mark" aria-hidden="true"></div>
    <div class="back__divider" aria-hidden="true"></div>
    <div class="back__details">
      <p class="back__person">Daniel Marsh</p>
      <p class="back__role">Founder &amp; MD</p>
      <p class="back__contact">
        <span class="back__accent">daniel</span>@velarix.com<br>
        <span class="back__accent">mobile:</span> 0821457730&nbsp;&nbsp;<span class="back__accent">office:</span> 010 448 2951
      </p>
      <p class="back__company">Velarix (Pty) Ltd</p>
      <p class="back__address">Suite 204, 18 Marlowe Rd, Parkhurst,<br>JHB, RSA</p>
    </div>
  </section>
</main>
</body>
</html>
```